Renewable energy website needs a wordpress website

We are a Renewable Energy company specialising in Energy Management, LED Lights and Solar PV Systems based in Kuala Lumpur.
We need wordpress website designed to match our company identity.
We would like to stick with similar shades of blue & green as our logo and to keep it fresh and creative at the same time.

```html
<!DOCTYPE html>
<html lang="en">
<head>
<meta charset="utf-8">
<title>Verdanta Power</title>
<link rel="stylesheet" href="https://fonts.googleapis.com/css2?family=Questrial&family=Lato:ital,wght@0,400;0,700;1,700&display=swap">
<style>
:root{
  --green:#7cb32f;
  --green-dark:#0a3a22;
  --footer:#033a1e;
  --cyan:#00bfdc;
  --blue:#1aa8e0;
  --text:#555;
  --line:#d8d8d8;
  --white:#fff;
}
*{box-sizing:border-box;margin:0;padding:0}
html,body{width:921px;height:1200px;overflow:hidden;background:var(--white)}
body{font-family:'Lato',sans-serif;color:var(--text);font-size:11px}
.page{position:relative;width:921px;height:1200px;overflow:hidden}
.abs{position:absolute}
.display{font-family:'Questrial',sans-serif}

/* header */
.logo{left:94px;top:12px;display:flex;align-items:center;gap:8px}
.logo-dot{width:36px;height:36px;border-radius:50%;background:var(--cyan)}
.logo-name{font-family:'Questrial',sans-serif;font-size:18px;color:var(--cyan);line-height:1}
.call{right:82px;top:5px;font-size:9px;font-style:italic;font-weight:700;color:#222}
.call span{color:var(--green)}
.nav{left:425px;top:31px;display:flex;align-items:center;font-size:9.5px;color:var(--cyan)}
.nav a{color:var(--cyan);text-decoration:none;padding:0 7px}
.nav .sep{color:var(--cyan)}
.nav .active{background:var(--green);color:var(--white);padding:6px 12px}

/* hero */
.hero{left:0;top:63px;width:921px;height:293px;background:linear-gradient(180deg,#4a86d6 0%,#7aaee4 45%,#2c5fae 100%)}
.hero-arrow{top:136px}
.hero-line{left:88px;color:var(--white);font-family:'Questrial',sans-serif;font-size:28px;font-weight:700;padding:0 12px;line-height:36px;white-space:nowrap}
.l1{top:144px;background:var(--green)}
.l2{top:182px;background:var(--cyan)}
.l3{top:221px;background:var(--green-dark)}

/* newsletter band */
.band{left:0;top:356px;width:921px;height:65px;background:var(--cyan)}
.band h2{left:88px;top:8px;font-family:'Questrial',sans-serif;font-size:17px;color:var(--white);font-weight:700}
.band p{left:88px;top:30px;font-family:'Questrial',sans-serif;font-size:11px;color:var(--white);line-height:14px}
.field{background:var(--white);border:1px solid #cfd6da;color:#999;font-size:9px;padding:0 7px;display:flex;align-items:center}
.btn-green{background:var(--green);color:var(--white);font-family:'Questrial',sans-serif;font-weight:700;display:flex;align-items:center;justify-content:center;border:1px solid #fff}
.btn-blue{background:linear-gradient(#3fc6ee,#14a2dd);color:var(--white);font-family:'Questrial',sans-serif;display:flex;align-items:center;justify-content:center;border:1px solid #0d8dc3}

/* welcome */
.welcome{left:90px;top:446px;width:520px;font-family:'Questrial',sans-serif;font-size:15px;color:var(--cyan);border-bottom:1px dashed var(--green);padding-bottom:4px}
.welcome b{color:var(--green);font-size:18px}
.body-copy{font-size:10.5px;line-height:15px;color:var(--text)}
.video{left:288px;top:485px;width:323px;height:197px;background:#2b2b2b}
.video-title{left:8px;top:14px;color:#eee;font-size:8px}
.video-frame{left:4px;top:27px;width:315px;height:147px;background:radial-gradient(circle at 50% 55%,#cfe6c9 0%,#5cb85c 35%,#e8e8e8 60%,#d9d9d9 100%)}
.phone{color:var(--cyan);font-style:italic;font-weight:700}

/* cards */
.card{width:164px;height:186px;border:1px solid var(--line);box-shadow:0 0 3px rgba(0,0,0,.08);background:var(--white)}
.card-img{left:6px;top:6px;width:152px;height:83px}
.card h3{left:0;top:98px;width:100%;text-align:center;font-family:'Questrial',sans-serif;font-size:12px;font-weight:700;color:var(--green)}
.card p{left:6px;top:118px;width:152px;font-size:8.5px;line-height:11px}
.card a{left:6px;top:168px;font-size:8px;color:var(--cyan);font-weight:700}

/* sidebar */
.side-box{width:200px;border:1px solid var(--line);box-shadow:0 0 3px rgba(0,0,0,.08);background:var(--white)}
.side-head{left:4px;top:5px;width:190px;height:25px;color:var(--white);font-family:'Questrial',sans-serif;font-size:15px;font-weight:700;display:flex;align-items:center;justify-content:center}
.quote-field{left:11px;width:177px;height:20px;font-size:8.5px}
.badge{width:52px;height:52px;border-radius:50%}

/* bottom promos */
.promo-green{left:83px;top:1007px;width:450px;height:110px;background:var(--green)}
.promo-blue{left:540px;top:1007px;width:284px;height:110px;background:var(--blue)}
.promo-green h2,.promo-blue h2{font-family:'Questrial',sans-serif;font-size:15px;font-weight:700;color:var(--white)}
.benefits{left:18px;top:34px;list-style:none;color:var(--white);font-size:8.5px;font-style:italic;font-weight:700;line-height:15px}
.benefits li::before{content:"•";margin-right:6px}

/* footer */
.footer{left:0;top:1131px;width:921px;height:69px;background:var(--footer);color:var(--white);font-family:'Questrial',sans-serif;font-size:10px}
.foot-div{top:10px;width:1px;height:48px;background:#1d5a38}
.social{width:18px;height:18px;border-radius:2px}
</style>
</head>
<body>
<div class="page">

  <!-- header -->
  <div class="abs logo"><span class="logo-dot"></span><span class="logo-name">VERDANTA POWER</span></div>
  <div class="abs call">Call Us: <span>+603 5550 1234</span></div>
  <nav class="abs nav">
    <a class="active">Home</a><a>About Us</a><span class="sep">|</span><a>Products</a><span class="sep">|</span><a>Services</a><span class="sep">|</span><a>Why SunField Energy</a><span class="sep">|</span><a>Contacts</a><span class="sep">|</span><a>Join us</a>
  </nav>

  <!-- hero -->
  <div class="abs hero" role="img" aria-label="Three technicians installing solar panels under a blue sky"></div>
  <svg class="abs hero-arrow" style="left:42px" width="22" height="30" viewBox="0 0 22 30"><path d="M17 3 5 15l12 12" fill="none" stroke="#fff" stroke-width="5"/></svg>
  <svg class="abs hero-arrow" style="left:842px" width="22" height="30" viewBox="0 0 22 30"><path d="M5 3l12 12L5 27" fill="none" stroke="#fff" stroke-width="5"/></svg>
  <div class="abs hero-line l1" style="top:207px">SunField Energy –</div>
  <div class="abs hero-line l2" style="top:245px">The Solar Specialists Trusted</div>
  <div class="abs hero-line l3" style="top:284px">by Thousands of Malaysians</div>

  <!-- newsletter -->
  <section class="abs band">
    <h2 class="abs">Get our FREE monthly Newsletter</h2>
    <p class="abs">With top rated secrets,inspirational articles, workouts<br>&amp; expert tips that actually work! Yup FREE!</p>
    <svg class="abs" style="left:410px;top:12px" width="42" height="40" viewBox="0 0 42 40"><rect x="2" y="10" width="38" height="28" rx="3" fill="#e9eef1" stroke="#9fb3bf"/><path d="M2 12l19 14 19-14" fill="none" stroke="#9fb3bf" stroke-width="1.5"/><rect x="10" y="2" width="22" height="14" fill="#6ac6e8"/></svg>
    <div class="abs field" style="left:473px;top:22px;width:115px;height:22px">First Name</div>
    <div class="abs field" style="left:593px;top:22px;width:115px;height:22px">Last Name</div>
    <div class="abs btn-green" style="left:714px;top:22px;width:79px;height:22px;font-size:12px">Yes Please!</div>
  </section>

  <!-- welcome -->
  <h1 class="abs welcome">welcome to <b>Verdanta Power</b></h1>
  <p class="abs body-copy" style="left:90px;top:483px;width:190px">SunField Energy has earned the trust of thousands of Malaysians choosing to install solar panels in Malaysia due to the quality products and outstanding service we provide. Starting as a leading solar power supplier in Perth (Australia), SunField Energy now have offices throughout Asia such as Malaysia, Singapore, Brunei, Hong Kong and China aligning with the common objective of helping you keep your hard earned money where it should be and saving the earth by producing a cleaner power source through solar power energy.</p>

  <div class="abs video">
    <div class="abs video-title">SunField Energy Malaysia</div>
    <div class="abs video-frame" role="img" aria-label="Video still of a solar panel inside green circular graphics"></div>
    <svg class="abs" style="left:141px;top:85px" width="42" height="30" viewBox="0 0 42 30"><rect width="42" height="30" rx="6" fill="#1e1e1e"/><path d="M17 8l10 7-10 7z" fill="#fff"/></svg>
    <div class="abs" style="left:6px;top:178px;width:311px;height:2px;background:#555"></div>
    <svg class="abs" style="left:12px;top:183px" width="10" height="10" viewBox="0 0 10 10"><path d="M2 1l7 4-7 4z" fill="#aaa"/></svg>
    <div class="abs" style="left:56px;top:183px;font-size:7px;color:#ccc">0:00 / 3:49</div>
  </div>

  <p class="abs body-copy" style="left:92px;top:692px;width:520px">SunField Energy only use in-house trained and industry qualified electricians whom are extremely knowledgeable about solar power systems and perform all solar panel installations in Malaysia to the highest standards. We are able to provide a complete one stop service for all your solar power needs. This ensures you have a seamless hassle free experience when you get solar power panels in Malaysia with us.</p>
  <p class="abs body-copy" style="left:92px;top:767px;width:520px">For quality solar panels and to enquire about our service in Malaysia, contact the team of Malaysia's Solar Power experts on <span class="phone">+603 5550 1234.</span></p>

  <!-- service cards -->
  <article class="abs card" style="left:90px;top:805px">
    <div class="abs card-img" role="img" aria-label="Hand holding a glowing light against a dark blue background" style="background:linear-gradient(135deg,#0c1f4a,#4f7fc4 60%,#0b1a3a)"></div>
    <h3 class="abs">Energy Management</h3>
    <p class="abs">Donec id dignissim eros. Pellentesque diam sem, luctus et fermentum vitae, aliquam a nibh. Etiam turpis odio, lacinia quis turpis non, dictum laoreet erat.</p>
    <a class="abs">Read More</a>
  </article>
  <article class="abs card" style="left:266px;top:805px">
    <div class="abs card-img" role="img" aria-label="LED bulbs on a green background" style="background:linear-gradient(135deg,#8fd16a,#5fb246)"></div>
    <h3 class="abs">LED Lights</h3>
    <p class="abs">Donec id dignissim eros. Pellentesque diam sem, luctus et fermentum vitae, aliquam a nibh. Etiam turpis odio, lacinia quis turpis non, dictum laoreet erat.</p>
    <a class="abs">Read More</a>
  </article>
  <article class="abs card" style="left:441px;top:805px">
    <div class="abs card-img" role="img" aria-label="Rows of solar panels under blue sky" style="background:linear-gradient(180deg,#6fa8e8,#2d5fb0)"></div>
    <h3 class="abs">Solar PV Systems</h3>
    <p class="abs">Donec id dignissim eros. Pellentesque diam sem, luctus et fermentum vitae, aliquam a nibh. Etiam turpis odio, lacinia quis turpis non, dictum laoreet erat.</p>
    <a class="abs">Read More</a>
  </article>

  <!-- quote form -->
  <aside class="abs side-box" style="left:624px;top:438px;height:276px">
    <div class="abs side-head" style="background:var(--green)">Get A FREE Quote</div>
    <div class="abs field quote-field" style="top:41px">Name</div>
    <div class="abs field quote-field" style="top:66px">Phone No</div>
    <div class="abs field quote-field" style="top:90px">Email id</div>
    <div class="abs field quote-field" style="top:115px">State</div>
    <div class="abs field quote-field" style="top:139px">How did you know about us?</div>
    <div class="abs field quote-field" style="top:164px;height:69px;align-items:flex-start;padding-top:5px">Your Message</div>
    <div class="abs btn-blue" style="left:46px;top:243px;width:106px;height:23px;font-size:13px">Get A Quote</div>
  </aside>

  <!-- certificates -->
  <aside class="abs side-box" style="left:624px;top:724px;height:266px">
    <div class="abs side-head" style="background:var(--cyan)">Certificates</div>
    <div class="abs badge" style="left:22px;top:50px;background:#f2a23a"></div>
    <div class="abs" style="left:130px;top:50px;width:44px;height:60px;background:#1b1b1b"></div>
    <div class="abs" style="left:22px;top:145px;width:56px;height:40px;background:#d8282e"></div>
    <div class="abs badge" style="left:127px;top:138px;background:#1b3c7a"></div>
    <div class="abs" style="left:51px;top:215px;width:98px;height:30px;background:#2a8a4a"></div>
  </aside>

  <!-- promos -->
  <section class="abs promo-green">
    <h2 class="abs" style="left:10px;top:8px">Getlatest updates, benefits and discount offers!</h2>
    <p class="abs" style="left:10px;top:29px;color:#fff;font-size:9px">Subscribe to our FREE monthly newsletter  for news, updates and others importnat messages!</p>
    <div class="abs field" style="left:13px;top:59px;width:159px;height:27px">Your name</div>
    <div class="abs field" style="left:178px;top:59px;width:159px;height:27px">Your email id</div>
    <div class="abs btn-blue" style="left:343px;top:59px;width:109px;height:27px;font-size:15px;border-color:#fff">Sign Me Up!</div>
  </section>
  <section class="abs promo-blue">
    <h2 class="abs" style="left:10px;top:12px">Benefits of Solar Energy</h2>
    <ul class="abs benefits">
      <li>Lorem ipsum dolo adipiscing elit.</li>
      <li>Pellentesque iiaculis.</li>
      <li>Proin id masam.</li>
      <li>Etiam sed justo cursus.</li>
    </ul>
    <div class="abs" role="img" aria-label="House roof fitted with solar panels" style="left:178px;top:16px;width:102px;height:84px;border:2px solid #fff;background:linear-gradient(180deg,#cfd9e2,#6b6f72 55%,#3a3f45)"></div>
  </section>

  <!-- footer -->
  <footer class="abs footer">
    <div class="abs" style="left:92px;top:18px">Products &nbsp;&nbsp;|&nbsp;&nbsp; Blog &nbsp;&nbsp;|&nbsp;&nbsp; Contact</div>
    <div class="abs" style="left:92px;top:43px;font-size:8.5px">© 2014 verdanta power</div>
    <div class="abs foot-div" style="left:272px"></div>
    <div class="abs" style="left:305px;top:18px;line-height:14px">18 Jalan Maju 2/6, Taman Cahaya Industri,<br>47100 Sample Town, Selangor, Malaysia</div>
    <div class="abs foot-div" style="left:565px"></div>
    <div class="abs" style="left:600px;top:18px;line-height:14px">P: +603 5550 1234<br>F: +603 5550 1299</div>
    <div class="abs foot-div" style="left:705px"></div>
    <div class="abs social" style="left:722px;top:21px;background:#3b5998"></div>
    <div class="abs social" style="left:747px;top:21px;background:#41a7dd"></div>
    <div class="abs social" style="left:772px;top:21px;background:#d8362a"></div>
    <div class="abs social" style="left:797px;top:21px;background:#5a7d9a"></div>
  </footer>

</div>
</body>
</html>
```